FUN Sizing Chart for Apparel Company.

We are a company called GROAN, we make cycling jerseys for the fun lovers and beer enthusiasts.....they might even like to bike. www.groankitvale.com We need a nice looking, but more importantly fun sizing chart created that reflects our personality. I've attached the sizing provided by the manufacturer with some information omitted --- what they provided was overkill and confusing, we just need chest measurements. Please create the graphic so that we can somewhat easily adjust the measurements should our pattern change.

FUN is the big winner. Our brand represents light-heartedness. For example, we chose to size our jerseys in volumes of beer which may or may not be incorporated into the graphic:
X-Small = The Half-Pint
Small = The Pint
Medium = The Bomber
Large = The Forty
X-Large = The Growler
XX-Large = The Pony Keg
XXX-Large = The Keg

Industry/Entity Type

It Company

```html
<!DOCTYPE html>
<html lang="en">
<head>
<meta charset="utf-8">
<title>GROAN Jersey Sizing Chart</title>
<link rel="stylesheet" href="https://fonts.googleapis.com/css2?family=Arimo:wght@400;700&family=Mali:wght@500&display=swap">
<style>
  :root {
    --paper: #ffffff;
    --ink: #000000;
    --rule: #555555;
    --women: #d9bde2;
    --men: #9399e0;
    --beer: rgba(243, 201, 40, 0.85);
    --foam: rgba(253, 240, 170, 0.6);
    --rider: rgba(40, 40, 40, 0.35);
    --clear: rgba(255, 255, 255, 0);
  }
  html, body {
    margin: 0;
    padding: 0;
    overflow: hidden;
  }
  body {
    width: 927px;
    height: 1200px;
    background: var(--paper);
    position: relative;
    font-family: "Arimo", Arial, sans-serif;
    color: var(--ink);
  }
  .size-chart {
    position: absolute;
    left: 102px;
    top: 111px;
    width: 731px;
    border-collapse: collapse;
    table-layout: fixed;
  }
  .size-chart td, .size-chart th {
    border: 1px solid var(--rule);
    padding: 0;
    text-align: center;
    vertical-align: middle;
  }
  .chart-intro {
    height: 89px;
    font-weight: 700;
    font-size: 17px;
    letter-spacing: 0.7px;
    line-height: 23.5px;
  }
  .size-chart td.chart-intro {
    vertical-align: top;
    padding-top: 2px;
  }
  .col-head th {
    height: 71px;
    font-size: 17px;
    letter-spacing: 0.7px;
    line-height: 23px;
    font-weight: 700;
  }
  .size-row td { height: 60px; }
  .measure { font-weight: 700; font-size: 17.5px; letter-spacing: 0.6px; }
  .standard { font-size: 16px; }
  .women { background: var(--women); }
  .men { background: var(--men); }
  .beer-size {
    font-family: "Mali", "Comic Sans MS", cursive;
    font-size: 23px;
    font-weight: 500;
  }
  .beer-illustration {
    position: absolute;
    left: 228px;
    top: 704px;
    width: 448px;
    height: 296px;
    background:
      radial-gradient(closest-side, var(--rider), var(--clear)) 250px 150px / 200px 146px no-repeat,
      radial-gradient(closest-side, var(--beer), var(--foam) 55%, var(--clear)) 0 150px / 260px 146px no-repeat,
      radial-gradient(closest-side, var(--foam), var(--clear)) 140px 0 / 260px 190px no-repeat;
  }
</style>
</head>
<body>
  <table class="size-chart">
    <colgroup>
      <col style="width:111px"><col style="width:198px"><col style="width:102px"><col style="width:191px"><col style="width:129px">
    </colgroup>
    <tr>
      <td class="chart-intro" colspan="5">GROAN T-Shirt sizes are based on your chest size<br>(Get those tape measures ready!)<br>Refer to this chart to help you find the best size.</td>
    </tr>
    <tr class="col-head">
      <th>Women’s<br>Chest<br>Size</th>
      <th class="women">Women's<br>GROAN Size</th>
      <th>Men’s<br>Chest<br>Size</th>
      <th class="men">Men's<br>GROAN Size</th>
      <th>Standard<br>Sizes</th>
    </tr>
    <tr class="size-row">
      <td class="measure">34”</td><td class="women beer-size">The Half Pint</td>
      <td></td><td></td><td class="standard">Extra Small</td>
    </tr>
    <tr class="size-row">
      <td class="measure">36 “</td><td class="women beer-size">The Pint</td>
      <td class="measure">40”</td><td class="men beer-size">The Pint</td><td class="standard">Small</td>
    </tr>
    <tr class="size-row">
      <td class="measure">38”</td><td class="women beer-size">The Bomber</td>
      <td class="measure">42.5”</td><td class="men beer-size">The Bomber</td><td class="standard">Medium</td>
    </tr>
    <tr class="size-row">
      <td class="measure">40”</td><td class="women beer-size">The Forty</td>
      <td class="measure">45”</td><td class="men beer-size">The Forty</td><td class="standard">Large</td>
    </tr>
    <tr class="size-row">
      <td class="measure">42.5”</td><td class="women beer-size">The Growler</td>
      <td class="measure">47.5</td><td class="men beer-size">The Growler</td><td class="standard">X Large</td>
    </tr>
    <tr class="size-row">
      <td class="measure">45”</td><td class="women beer-size">The Pony Keg</td>
      <td class="measure">50</td><td class="men beer-size">The Pony Keg</td><td class="standard">XX Large</td>
    </tr>
    <tr class="size-row">
      <td></td><td></td>
      <td class="measure">52.5</td><td class="men beer-size">The Keg</td><td class="standard">XXX Large</td>
    </tr>
  </table>

  <div class="beer-illustration" role="img" aria-label="Illustration of a tipped beer keg spilling foamy beer with rising bubbles, beside a cyclist pictogram on a bicycle"></div>
</body>
</html>
```